Webdesign für freie Trauungen
Zielgruppe
Webseite für Hochzeitspaare, Trauerende, Bestatter, Interessierte
Aufgabenstellung
Internetseite
Briefing:
Onepager
Internetseite soll wirken:
Modern
Schlank
Klar
Vertrauenserweckend
professionell
Home:
Reden für besondere Momente im Leben
Schrift an Flyer anpassen
REDEN.
ERZÄHLEN.
ERINNERN.
BERÜHREN.
Bild von mir,
Dazu, meine Reden sind:
freundlich
authentisch
ehrlich
einfühlsam
taktvoll
humorvoll
tiefsinnig
tröstend
nett
zugewandt
interessant
nach Euren Wünschen
mit Euren Inhalten
individuell
sehr persönlich
kreativ
wortgewandt
erfahren
Sprechen Sie mich an! ?
FREIE TRAUUNG:
EINFACH HIMMLISCH!
eine Liebesgeschichte erzählen
Sich ein Versprechen geben
JA zueinander sagen
Mit lieben Menschen feiern
wo, wann, wie - das entscheidet Ihr!
Segensfeier - Willkommensfeier:
im Leben willkommen heißen
Was bedeutet der Name des Kindes?
Was wollt Ihr Eurem Kind mitgeben?
Was wünscht Ihr Euch für Euer Kind?
TRAUERFEIER:
an schöne Momente erinnern
Einen Menschen mit Worten lebendig werden lassen
Mit einer persönlichen und bewegenden Ansprache
Mit all dem, was Sie sich wünschen!
REDEN ZU GEBURTSTAGEN:
mit Humor, Witz und Verstand gemeinsam zurück schauen
Und von Träumen und Sehnsüchten erzählen
Reden zum Jubiläum:
gemeinsam zurück schauen
Geleistetes würdigen
Veränderungen verständlich machen
Ausblicke wagen
Biographien:
festhalten, damit nichts von Ihrer Lebensgeschichte verloren geht
Sie erinnern sich und ich schreibe auf
Referenzen:
???? Wie am besten ???
Persönliches Vita:
Studium an der Offenen Hochschule Berlin:
- Publizistik
Germanistik
Volkswirtschaftslehre
Lateinamerikanistik
Abschluß: Magistra Artium
Freie Rednerin seit 1998
Telefonnummer 015239870461
Email: doris.Kellmeyer@postfeld.de
Wirk..

```html
<!DOCTYPE html>
<html lang="de">
<head>
<meta charset="utf-8">
<title>Kellmeyer Reden</title>
<link rel="stylesheet" href="https://fonts.googleapis.com/css2?family=Source+Sans+3:wght@300;400;600&family=Oxygen:wght@300;400&display=swap">
<style>
:root{
  --teal:#5e9792;
  --ink:#3a3a3a;
  --text:#555;
  --muted:#7a7a7a;
  --panel:#f3f5f4;
  --dark:#333436;
  --white:#fff;
}
*{margin:0;padding:0;box-sizing:border-box}
html,body{width:1200px;height:2469px;overflow:hidden}
body{position:relative;background:var(--white);font-family:"Oxygen",sans-serif;color:var(--text)}
.abs{position:absolute}
.head-font{font-family:"Source Sans 3",sans-serif}

/* header */
.site-header{left:0;top:0;width:1200px;height:86px}
.brand{left:56px;top:20px;font-family:"Source Sans 3",sans-serif;font-weight:400;font-size:24px;color:var(--ink);line-height:1;letter-spacing:1px}
.brand small{display:block;font-size:12px;letter-spacing:9px;margin-top:4px;padding-left:34px}
.main-nav{right:60px;top:37px;display:flex;gap:38px;font-family:"Source Sans 3",sans-serif;font-size:11.5px;color:var(--ink)}
.main-nav .active{color:var(--teal);font-weight:600}

/* hero */
.hero-panel{left:0;top:86px;width:450px;height:499px;background:var(--panel)}
.hero-photo{left:450px;top:86px;width:750px;height:499px;background:linear-gradient(90deg,#6b6a62 0%,#9b8f7e 30%,#5c5f5e 50%,#b7a98f 70%,#4d5250 100%)}
.hero-title{left:136px;top:210px;font-family:"Source Sans 3",sans-serif;font-weight:300;font-size:39px;line-height:44px;color:var(--ink)}
.hero-sub{left:136px;top:418px;font-family:"Source Sans 3",sans-serif;font-size:17px;line-height:21px;color:var(--teal)}

/* speeches */
.speeches{left:0;top:585px;width:1200px;height:908px;background:radial-gradient(ellipse at 45% 60%,#e6e9eb 0%,#d9dee2 45%,#f6f7f7 95%)}
.section-title{font-family:"Source Sans 3",sans-serif;font-weight:300;font-size:30px;color:var(--ink)}
.speeches .section-title{left:0;width:1200px;top:83px;text-align:center}
.qualities{left:0;width:1200px;top:157px;text-align:center;font-size:13.5px;line-height:20px;color:var(--text)}
.card{position:absolute;width:277px;height:257px;background:var(--white);box-shadow:0 6px 20px rgba(80,90,100,.12)}
.card .quote{position:absolute;left:18px;top:-11px;width:32px;height:32px;background:var(--teal)}
.card h3{position:absolute;left:44px;top:56px;font-family:"Source Sans 3",sans-serif;font-weight:400;font-size:17px;line-height:21px;color:var(--teal);text-transform:uppercase}
.card p{position:absolute;left:44px;right:20px;font-size:11px;line-height:15.7px;color:var(--text)}

/* vita */
.vita .section-title{left:136px;top:1555px}
.vita-h{font-family:"Source Sans 3",sans-serif;font-size:17px;line-height:21px;color:var(--teal)}
.study-list{list-style:none;font-size:12px;line-height:18.3px;color:var(--muted)}
.study-list li::before{content:"";display:inline-block;width:4px;height:4px;background:#888;margin-right:12px;vertical-align:middle}
.contact-box{left:386px;top:1649px;width:222px;height:285px;background:var(--panel)}
.contact-box h4{position:absolute;left:37px;top:96px}
.contact-box p{position:absolute;left:37px;font-size:12px;color:var(--ink)}
.portrait{left:637px;top:1649px;width:427px;height:285px;background:linear-gradient(100deg,#5a4a3e 0%,#cbb89a 35%,#8d7c66 60%,#3f6253 100%)}
.cta{left:897px;top:1954px;width:167px;height:32px;background:var(--teal);color:var(--white);font-family:"Source Sans 3",sans-serif;font-weight:600;font-size:11px;text-align:center;line-height:32px}

/* testimonials */
.testimonials{left:0;top:2049px;width:1200px;height:363px;background:linear-gradient(160deg,#e4e9ea 0%,#f3f5f5 50%,#e2e8e8 100%)}
.testimonials .section-title{left:0;width:1200px;top:67px;text-align:center}
.avatar{left:562px;top:131px;width:76px;height:76px;border-radius:50%;background:radial-gradient(circle at 50% 45%,#e2b58f 0%,#c9905f 60%,#8d6a50 100%)}
.quote-text{left:0;width:1200px;top:228px;text-align:center;font-size:12px;line-height:16px;color:var(--muted)}
.quote-name{left:0;width:1200px;top:276px;text-align:center;font-size:12px;color:var(--ink)}
.dots{left:580px;top:306px;display:flex;gap:6px}
.dots span{width:9px;height:9px;border-radius:50%;background:var(--white)}
.dots span.on{background:var(--teal)}

/* footer */
.site-footer{left:0;top:2412px;width:1200px;height:57px;background:var(--dark);color:var(--white);font-family:"Source Sans 3",sans-serif;font-size:11.5px}
.footer-brand{position:absolute;left:50px;top:14px;font-size:18px;line-height:1}
.footer-brand small{display:block;font-size:9px;letter-spacing:7px;padding-left:22px;margin-top:2px}
.footer-nav{position:absolute;left:440px;top:22px;display:flex;gap:28px}
.copyright{position:absolute;right:60px;top:23px;font-size:11px}
</style>
</head>
<body>

<header class="abs site-header">
  <div class="abs brand">Kellmeyer<small>REDEN</small></div>
  <nav class="abs main-nav">
    <span class="active">STARTSEITE</span><span>MEINE REDEN</span><span>PERSÖNLICHES VITA</span><span>REFERENZEN</span>
  </nav>
</header>

<section>
  <div class="abs hero-panel"></div>
  <div class="abs hero-photo" role="img" aria-label="Porträtfoto der Rednerin in Lederjacke, gespiegelt an einer Glasscheibe"></div>
  <h1 class="abs hero-title" style="font-weight:300">REDEN.<br>ERZÄHLEN.<br>ERINNERN.<br>BERÜHREN.</h1>
  <p class="abs hero-sub">REDEN FÜR BESONDERE<br>MOMENTE IM LEBEN</p>
</section>

<section class="abs speeches" role="img" aria-label="Sanfter Hintergrund mit Wasserwellen">
  <h2 class="abs section-title">MEINE REDEN SIND</h2>
  <p class="abs qualities">freundlich, authentisch, ehrlich, einfühlsam, taktvoll, humorvoll, tiefsinnig, tröstend, nett, zugewandt, interessant,<br>nach Euren Wünschen, mit Euren Inhalten, individuell, sehr persönlich, kreativ, wortgewandt, erfahren</p>
</section>

<svg width="0" height="0" style="position:absolute">
  <symbol id="quote-mark" viewBox="0 0 32 32"><path fill="#fff" d="M9 11h6v5l-3 5h-2.5l2-4H9zM17 11h6v5l-3 5h-2.5l2-4H17z"/></symbol>
</svg>

<article class="card" style="left:136px;top:867px">
  <span class="quote"><svg width="32" height="32"><use href="#quote-mark"/></svg></span>
  <h3>Freie Trauung:<br>Einfach himmlisch!</h3>
  <p style="top:112px">eine Liebesgeschichte erzählen<br>Sich ein Versprechen geben<br>JA zueinander sagen<br>Mit lieben Menschen feiern<br><br>wo, wann, wie - das entscheidet Ihr!</p>
</article>
<article class="card" style="left:461px;top:867px">
  <span class="quote"><svg width="32" height="32"><use href="#quote-mark"/></svg></span>
  <h3>Segensfeier<br>Willkommensfeier</h3>
  <p style="top:106px">im Leben willkommen heißen<br>Was bedeutet der Name des Kindes?<br>Was wollt Ihr Eurem Kind mitgeben?<br>Was wünscht Ihr Euch für Euer Kind?</p>
</article>
<article class="card" style="left:787px;top:867px">
  <span class="quote"><svg width="32" height="32"><use href="#quote-mark"/></svg></span>
  <h3>Trauerfeier</h3>
  <p style="top:106px">an schöne Momente erinnern<br>Einen Menschen mit Worten<br>lebendig werden lassen<br>Mit einer persönlichen und<br>bewegenden Ansprache<br>Mit all dem, was Sie sich wünschen!</p>
</article>
<article class="card" style="left:136px;top:1170px">
  <span class="quote"><svg width="32" height="32"><use href="#quote-mark"/></svg></span>
  <h3>Reden zu<br>Geburtstagen</h3>
  <p style="top:106px">mit Humor, Witz und Verstand<br>gemeinsam zurück schauen<br>Und von Träumen und Sehnsüchten<br>erzählen</p>
</article>
<article class="card" style="left:461px;top:1170px">
  <span class="quote"><svg width="32" height="32"><use href="#quote-mark"/></svg></span>
  <h3>Reden zum<br>Jubiläum</h3>
  <p style="top:106px">gemeinsam zurück schauen<br>Geleistetes würdigen<br>Veränderungen verständlich machen<br>Ausblicke wagen</p>
</article>
<article class="card" style="left:787px;top:1170px">
  <span class="quote"><svg width="32" height="32"><use href="#quote-mark"/></svg></span>
  <h3>Biographien</h3>
  <p style="top:106px">festhalten, damit nichts von Ihrer<br>Lebensgeschichte verloren geht<br>Sie erinnern sich und ich schreibe<br>auf</p>
</article>

<section class="vita">
  <h2 class="abs section-title">PERSÖNLICHES VITA</h2>
  <h4 class="abs vita-h" style="left:136px;top:1647px">STUDIUM AN DER OFFENEN<br>HOCHSCHULE BERLIN</h4>
  <ul class="abs study-list" style="left:136px;top:1700px">
    <li>Publizistik</li><li>Germanistik</li><li>Volkswirtschaftslehre</li><li>Lateinamerikanistik</li><li>Abschluß: Magistra Artium</li>
  </ul>
  <h4 class="abs vita-h" style="left:136px;top:1820px">FREIE REDNERIN SEIT 1998</h4>
  <h4 class="abs vita-h" style="left:137px;top:1869px">WIRKUNGSKREIS</h4>
  <p class="abs" style="left:137px;top:1898px;font-size:12px;line-height:18.5px;color:var(--muted)">Aachen, Viersen, Düsseldorf,<br>Krefeld, Erkelenz, Neuss, Köln</p>

  <div class="abs contact-box">
    <h4 class="vita-h">KONTAKT</h4>
    <p style="top:133px">doris.kellmeyer@postfeld.de</p>
    <p style="top:160px">0152-39870461</p>
    <p style="top:187px;color:var(--teal);font-size:11px">kellmeyerreden.de</p>
  </div>
  <div class="abs portrait" role="img" aria-label="Porträtfoto der Rednerin mit Brille vor einem grünen Samtsessel"></div>
  <div class="abs cta">SPRECHEN SIE MICH AN!</div>
</section>

<section class="abs testimonials">
  <h2 class="abs section-title">DAS SAGEN KUNDEN ÜBER MICH</h2>
  <div class="abs avatar" role="img" aria-label="Kundenfoto"></div>
  <p class="abs quote-text">Sed eiusmod tempor incidunt ut labore et dolore magna aliqua. Ut enim ad minim veniam, quis<br>nostrud exercitation ullamco laboris nisi ut aliquid ex ea commodi consequat.</p>
  <p class="abs quote-name">Miriam Musterfrau</p>
  <div class="abs dots"><span class="on"></span><span></span><span></span></div>
</section>

<footer class="abs site-footer">
  <div class="footer-brand">Kellmeyer<small>REDEN</small></div>
  <nav class="footer-nav"><span>STARTSEITE</span><span>KONTAKT</span><span>IMPRESSUM</span><span>DATENSCHUTZ</span></nav>
  <div class="copyright">COPYRIGHT @2021 DORIS KELLMEYER</div>
</footer>

</body>
</html>
```